Business card design for Virtual Assistance company

I need a business card designed for my virtual assistance company. We are a small company who services primarily C-level executive clients. The card needs to be double sided with the following contact information on the back:
Melanie Hartwick
Owner/CEO
info@pbtadvisory.net
www.pbtadvisory.net
240.395.2817

The front side should just have the company name incorporated: "PBT Advisory" and "virtual assistance"

The card should be simplistic, but eye catching and should speak to high level executives. Our primary focus areas consist of executive assistance and government contracting.

Target Market(s)

CEOs and executives

Contact Information for Business Card

see project description. phone, email, website.

Colors

Designer to choose only greyscale colors for use in the design.

```html
<!DOCTYPE html>
<html lang="en">
<head>
<meta charset="utf-8">
<title>PBT Advisory — Business Card</title>
<link rel="stylesheet" href="https://fonts.googleapis.com/css2?family=Libre+Baskerville:wght@400;700&family=Montserrat:wght@300;400&display=swap">
<style>
  :root {
    --stage: #3a3633;
    --card: #141414;
    --card-back: #0c0c0c;
    --ink: #f4f4f4;
    --ink-soft: #d6d6d6;
    --rule: #bdbdbd;
    --mark: #232323;
  }
  * { box-sizing: border-box; margin: 0; padding: 0; }
  html, body { width: 1200px; height: 786px; overflow: hidden; }
  body {
    background: var(--stage);
    display: flex;
    align-items: center;
    justify-content: center;
    gap: 40px;
  }
  .card {
    width: 540px;
    height: 309px;
    border-radius: 3px;
    position: relative;
  }
  .card--contact {
    background: var(--card);
    display: flex;
    align-items: center;
    padding: 0 36px 0 40px;
  }
  .brand {
    width: 220px;
    text-align: center;
    margin-top: 60px;
  }
  .brand__name {
    font-family: "Libre Baskerville", serif;
    font-weight: 400;
    font-size: 25px;
    color: var(--ink);
    letter-spacing: 0.2px;
  }
  .brand__tagline {
    font-family: "Libre Baskerville", serif;
    font-size: 10.5px;
    letter-spacing: 1.6px;
    color: var(--ink-soft);
    margin-top: 4px;
  }
  .divider {
    width: 1px;
    height: 104px;
    background: var(--rule);
    margin: 0 20px 0 18px;
  }
  .person__name {
    font-family: "Libre Baskerville", serif;
    font-weight: 700;
    font-size: 17px;
    color: var(--ink);
  }
  .person__role {
    font-family: "Montserrat", sans-serif;
    font-weight: 300;
    font-size: 12px;
    color: var(--ink-soft);
    margin: 3px 0 9px;
  }
  .contact-list { list-style: none; }
  .contact-list li {
    display: flex;
    align-items: center;
    gap: 8px;
    font-family: "Montserrat", sans-serif;
    font-weight: 300;
    font-size: 12px;
    color: var(--ink);
    line-height: 1.9;
  }
  .contact-list svg { width: 11px; height: 11px; fill: var(--ink); flex: none; }
  .card--front {
    background: var(--card-back);
    display: flex;
    align-items: center;
    justify-content: center;
  }
  .front__name {
    font-family: "Libre Baskerville", serif;
    font-weight: 400;
    font-size: 52px;
    color: var(--mark);
  }
</style>
</head>
<body>
  <section class="card card--contact">
    <div class="brand">
      <p class="brand__name">PBT Advisory</p>
      <p class="brand__tagline">VIRTUAL ASSISTANCE</p>
    </div>
    <div class="divider"></div>
    <div class="person">
      <p class="person__name">Melanie Hartwick</p>
      <p class="person__role">Owner/CEO</p>
      <ul class="contact-list">
        <li>
          <svg viewBox="0 0 24 24" aria-hidden="true"><path d="M6.6 10.8a15 15 0 0 0 6.6 6.6l2.2-2.2c.3-.3.7-.4 1-.2 1.1.4 2.3.6 3.6.6.6 0 1 .4 1 1V20c0 .6-.4 1-1 1A17 17 0 0 1 3 4c0-.6.4-1 1-1h3.5c.6 0 1 .4 1 1 0 1.3.2 2.5.6 3.6.1.3 0 .7-.2 1z"/></svg>
          240.395.2817
        </li>
        <li>
          <svg viewBox="0 0 24 24" aria-hidden="true"><path d="M2 5h20v2l-10 6L2 7zM2 9l10 6 10-6v10H2z"/></svg>
          info@pbtadvisory.net
        </li>
        <li>
          <svg viewBox="0 0 24 24" aria-hidden="true"><path d="M12 2a10 10 0 1 0 0 20 10 10 0 0 0 0-20zm-1 17.9A8 8 0 0 1 4.1 10L9 15v1a2 2 0 0 0 2 2zm6.9-2.5A2 2 0 0 0 16 16h-1v-3a1 1 0 0 0-1-1H8v-2h2a1 1 0 0 0 1-1V7h2a2 2 0 0 0 2-2v-.4a8 8 0 0 1 2.9 12.8z"/></svg>
          www.pbtadvisory.net
        </li>
      </ul>
    </div>
  </section>
  <section class="card card--front">
    <p class="front__name">PBT Advisory</p>
  </section>
</body>
</html>
```